furnace plenum sticker

This sticker is left at every job above the furnace or on the duct work connected to the furnace.
It needs to be bold so that when homeowner is at the furnace during a break down they see it. Phone number and what we do needs to be prominate. It is our calling card for service.
Sticker needs to look corporate and professional.

New logo (attached) must be incorporated into sticker.

Current sticker attached
Size
8.5 inches x 5.5 inches

Target Market(s)

residential home owners

Industry/Entity Type

Work

Colors
ec1f27

Requirements
Must have
• Our new current logo attached

```html
<!DOCTYPE html>
<html lang="en">
<head>
<meta charset="utf-8">
<title>Northfield Heating and Air Conditioning – Furnace Sticker</title>
<link href="https://fonts.googleapis.com/css2?family=Open+Sans:wght@700;800&display=swap" rel="stylesheet">
<style>
  :root {
    --page-bg: #e6e4e1;
    --sticker-white: #f2f2f2;
    --brand-red: #ec1f27;
    --panel-red: #c4524e;
    --frame-blue: #3f5f8a;
    --ink: #111111;
  }
  * { box-sizing: border-box; margin: 0; padding: 0; }
  html, body {
    width: 1200px; height: 1200px; overflow: hidden;
    background: var(--page-bg);
    font-family: "Open Sans", Arial, sans-serif;
  }
  .canvas {
    width: 1200px; height: 1200px;
    display: flex; align-items: center; justify-content: center;
  }
  .sticker {
    width: 1100px; height: 712px;
    display: flex;
    box-shadow: 0 6px 24px rgba(0,0,0,0.18);
  }
  .brand-side {
    width: 48%;
    background: var(--sticker-white);
    display: flex; flex-direction: column; justify-content: center;
    padding: 0 60px;
  }
  .brand-mark {
    width: 34px; height: 34px;
    background: var(--brand-red);
    margin: 0 0 34px 40px;
  }
  .serviced-by {
    font-weight: 800; font-size: 28px; color: var(--ink);
    margin-bottom: 4px;
  }
  .brand-name {
    font-weight: 800; font-size: 60px; color: var(--brand-red);
    letter-spacing: 1px; line-height: 1.05;
  }
  .brand-tagline {
    font-weight: 700; font-size: 17px; color: var(--ink);
    letter-spacing: 1.5px; margin-top: 2px;
  }
  .contact-side {
    width: 52%;
    background: var(--panel-red);
    padding: 26px;
  }
  .contact-frame {
    height: 100%;
    border: 4px solid var(--frame-blue);
    padding: 30px 34px;
    display: flex; flex-direction: column; justify-content: space-between;
    color: var(--ink);
    text-transform: uppercase;
  }
  .region { border-bottom: 2px solid var(--ink); padding-bottom: 10px; }
  .region-name { font-weight: 800; font-size: 30px; letter-spacing: 1px; line-height: 1.1; }
  .region-phone { font-weight: 800; font-size: 62px; letter-spacing: 2px; line-height: 1.05; }
  .services {
    font-weight: 800; font-size: 30px; letter-spacing: 1px; line-height: 1.3;
    border-bottom: 2px solid var(--ink); padding-bottom: 10px;
  }
  .emergency { font-weight: 800; font-size: 44px; letter-spacing: 1px; }
</style>
</head>
<body>
<main class="canvas">
  <section class="sticker">
    <div class="brand-side">
      <div class="brand-mark"></div>
      <p class="serviced-by">Serviced by</p>
      <p class="brand-name">NORTHFIELD</p>
      <p class="brand-tagline">HEATING AND AIR CONDITIONING</p>
    </div>
    <div class="contact-side">
      <div class="contact-frame">
        <div class="region">
          <p class="region-name">Burlington/Hamilton</p>
          <p class="region-phone">905-555-0142</p>
        </div>
        <div class="region">
          <p class="region-name">Oakville/Milton</p>
          <p class="region-phone">905-555-0187</p>
        </div>
        <p class="services">We service all makes<br>and models. Repairs<br>and installations.</p>
        <p class="emergency">24 Hour Service</p>
      </div>
    </div>
  </section>
</main>
</body>
</html>
```